Banner Ad Needed for e-commerce website

We are Tinkerloft.com, and we need a new category banner for this page on our website: http://www.tinkerloft-example.com/wireless-driveway-alarms/

The image we have now is great, but it's the wrong size and is due for an update. Please post a design that follows the elements already found on our website.

Specifically, Sans serif font, clean lines and edges, with a basic, soft gradient in the background. Preferably gray.

We're not looking for special effects- we need something professional, subtle, and simple. Our audience is in the senior citizen category and therefore are not impressed by fancy graphics or lens flare, etc etc.Something easy to read and understand is best.

Positioning and placement of our products is KEY to a good banner.

Target Market(s)

Adults and senior citizens (30 years old+) Homeowners, people usually unfamiliar with using or navigating websites, etc. United States.

Industry/Entity Type

E-Commerce

Font styles to use
Sans Serif

Colors

Designer to choose colors to be used in the design.

Requirements
Must have
• It must have the words "Wireless Driveway Alarms".

The Pathwarden receiver must be included (pathwardenreceiver.jpg must be worked into the banner in some way. pathwardensensor.jpg is the other half of the set, but is optional)
In addition to the pathwardenreceiver.jpg image, you must showcase another driveway alarm set somewhere in the banner. You may pick any of them.

Black background, with a style similar to our website

DIMENSIONS: Must be 980x300 pixels.
Nice to have
• Please post one to three submissions that follow our guidelines closely. If you have multiple versions, pick your best examples.
Please ensure you cleanly cut our stock images from the white background- sloppy work here will be rejected!
Should not have
• Fancy fonts, effects, etc.

```html
<!DOCTYPE html>
<html lang="en">
<head>
<meta charset="utf-8">
<title>Wireless Driveway Alarms – Tinkerloft.com</title>
<link rel="stylesheet" href="https://fonts.googleapis.com/css2?family=Open+Sans:wght@700;800&display=swap">
<style>
  :root {
    --bg-light: #5e5e5e;
    --bg-mid: #4a4a4a;
    --bg-dark: #323232;
    --type-top: #ffffff;
    --type-bottom: #cfcfcf;
    --type-shadow: rgba(0, 0, 0, 0.55);
    --product-light: #4c4c4a;
    --product-dark: #1c1c1c;
  }
  html, body {
    margin: 0;
    padding: 0;
    width: 1200px;
    height: 367px;
    overflow: hidden;
    background: var(--bg-dark);
  }
  .banner {
    position: relative;
    width: 1200px;
    height: 367px;
    overflow: hidden;
    background: radial-gradient(ellipse 75% 95% at 45% 45%, var(--bg-light) 0%, var(--bg-mid) 55%, var(--bg-dark) 100%);
    font-family: "Open Sans", Arial, sans-serif;
  }
  .banner__title {
    position: absolute;
    left: 40px;
    top: 52px;
    margin: 0;
    font-weight: 800;
    line-height: 1;
    text-transform: uppercase;
    color: var(--type-top);
    text-shadow: 0 2px 3px var(--type-shadow);
  }
  .banner__title-line {
    display: block;
    background: linear-gradient(180deg, var(--type-top) 0%, var(--type-top) 45%, var(--type-bottom) 100%);
    -webkit-background-clip: text;
    background-clip: text;
  }
  .banner__title-line--small {
    font-size: 63px;
    letter-spacing: -1.5px;
  }
  .banner__title-line--large {
    margin-top: 2px;
    margin-left: -4px;
    font-size: 150px;
    letter-spacing: 1px;
  }
  .banner__products {
    position: absolute;
    left: 782px;
    top: 42px;
    width: 378px;
    height: 314px;
    border-radius: 18px;
    background: linear-gradient(160deg, var(--product-light) 0%, var(--product-dark) 100%);
  }
</style>
</head>
<body>
  <main class="banner">
    <h1 class="banner__title">
      <span class="banner__title-line banner__title-line--small">Wireless Driveway</span>
      <span class="banner__title-line banner__title-line--large">Alarms</span>
    </h1>
    <div class="banner__products" role="img" aria-label="Product photo: Pathwarden wireless driveway alarm receiver and sensor, shown together with a second alarm set from Northfield Alert including its sensor box and handheld receiver"></div>
  </main>
</body>
</html>
```